Business Card Design

I have a very clear idea of what I want. I just do not know how to do the graphic design to match it.

On the front I want the uploaded image with the horse and the two people.
I want

Bottom left hand corner
Lewis Brand
0438 512 607

Bottom right
There is maroon block with Neil Patton Practitioner Group Logo
Next to that I want the Stable Arc tile about the same size ( attached psd file)

On the back I want a plain colour (white) with the information

Lewis Brand
Equine Performance
Rowland4Ponies and Acupuncture
Horsemanship Lessons and Clinics
Horse Training

lbrand@fauna812.com.au
FB/lewis.brand.207
StableArc.com.au

Industry/Entity Type

Business

Contact Information for Business Card

Lewis Brand
0438 512 607
lbrand@fauna812.com.au

```html
<!DOCTYPE html>
<html lang="en">
<head>
<meta charset="utf-8">
<title>Lewis Brand – Business Card</title>
<link href="https://fonts.googleapis.com/css2?family=Cinzel:wght@500&family=Courgette&family=Kaushan+Script&family=Source+Sans+3:wght@400;600&display=swap" rel="stylesheet">
<style>
  :root{
    --backdrop:#cbcbcb;
    --sand-light:#e3c998;
    --sand-mid:#c9a46a;
    --sand-dark:#9c7a47;
    --ink-brown:#4a2612;
    --maroon:#5b2012;
    --tile:#ffffff;
    --tile-ink:#1f3f86;
    --card-dark:#343537;
    --band:#48494b;
    --on-dark:#ffffff;
  }
  *{margin:0;padding:0;box-sizing:border-box}
  html,body{width:1200px;height:1005px;overflow:hidden;background:var(--backdrop)}
  .card{position:absolute;left:310px;width:580px;height:340px;overflow:hidden;box-shadow:0 6px 14px rgba(0,0,0,.25)}
  .card--front{top:140px}
  .card--back{top:525px;background:var(--card-dark)}

  .front-photo{position:absolute;inset:0;
    background:radial-gradient(ellipse at 70% 60%,var(--sand-light),var(--sand-mid) 60%,var(--sand-dark))}
  .headline{position:absolute;left:0;top:0;width:580px;height:240px}
  .headline .arc-text{font-family:"Cinzel",serif;font-size:17px;fill:var(--ink-brown);letter-spacing:.5px}
  .headline .your{font-family:"Kaushan Script",cursive;font-size:28px;fill:var(--ink-brown)}
  .headline .potential{font-family:"Kaushan Script",cursive;font-size:66px;fill:var(--ink-brown)}
  .headline .swash{fill:none;stroke:var(--ink-brown);stroke-width:3;stroke-linecap:round}

  .front-contact{position:absolute;left:70px;top:250px;color:var(--ink-brown)}
  .front-contact .name{font-family:"Courgette",cursive;font-size:30px;line-height:1}
  .front-contact .phone{font-family:"Source Sans 3",sans-serif;font-weight:600;font-size:21px;margin-top:6px;letter-spacing:.5px}

  .partner-badge{position:absolute;left:452px;top:268px;width:52px;height:56px;background:var(--maroon)}
  .brand-tile{position:absolute;left:512px;top:266px;width:56px;height:56px;border-radius:10px;background:var(--tile);
    border:3px solid var(--maroon);display:flex;align-items:center;justify-content:center;text-align:center;
    font-family:"Source Sans 3",sans-serif;font-weight:600;font-size:11px;line-height:1.05;color:var(--tile-ink)}

  .brand-mark{position:absolute;left:70px;top:170px;font-family:"Source Sans 3",sans-serif;font-weight:600;font-size:32px;color:var(--on-dark)}
  .back-name{position:absolute;left:322px;top:34px;font-family:"Courgette",cursive;font-size:32px;color:var(--on-dark)}
  .contact-list{position:absolute;left:322px;top:100px;list-style:none;font-family:"Source Sans 3",sans-serif;font-size:17px;color:var(--on-dark)}
  .contact-list li{display:flex;align-items:center;gap:12px;height:25px}
  .contact-list svg{width:15px;height:15px;flex:none}
  .services-band{position:absolute;left:0;bottom:0;width:100%;height:78px;background:var(--band);
    display:flex;flex-direction:column;align-items:center;justify-content:center;
    font-family:"Source Sans 3",sans-serif;font-size:15.5px;line-height:1.35;color:var(--on-dark)}
</style>
</head>
<body>
  <section class="card card--front">
    <div class="front-photo" role="img" aria-label="Photo of a trainer in a hat watching a woman lead a dark bay horse across a sandy arena"></div>
    <svg class="headline" viewBox="0 0 580 240">
      <path id="headline-arc" d="M60 112 Q200 40 400 62" fill="none"/>
      <text class="arc-text"><textPath href="#headline-arc">HOW YOU EVER GONNA KNOW</textPath></text>
      <path class="swash" d="M62 120 Q220 48 410 56"/>
      <text class="your" x="185" y="128">Your</text>
      <text class="potential" x="90" y="188">Potential</text>
      <path class="swash" d="M60 206 Q140 186 250 192 Q330 196 400 175"/>
    </svg>
    <div class="front-contact">
      <div class="name">Lewis Brand</div>
      <div class="phone">0438 512 607</div>
    </div>
    <div class="partner-badge" aria-label="Neil Patton Practitioner Group"></div>
    <div class="brand-tile">Stable<br>Arc</div>
  </section>

  <section class="card card--back">
    <div class="brand-mark">Stable Arc</div>
    <div class="back-name">Lewis Brand</div>
    <ul class="contact-list">
      <li><svg viewBox="0 0 16 16"><path fill="#fff" d="M2 6c0-2 3-3 6-3s6 1 6 3v1h-3V6H5v1H2zM4 8h8l1 5H3z"/></svg>0438 512 607</li>
      <li><svg viewBox="0 0 16 16" fill="none" stroke="#fff" stroke-width="1.4"><circle cx="8" cy="8" r="6.3"/><ellipse cx="8" cy="8" rx="2.8" ry="6.3"/><path d="M1.7 8h12.6"/></svg>StableArc.com.au</li>
      <li><svg viewBox="0 0 16 16"><rect x="2" y="2" width="12" height="12" rx="2" fill="#fff"/></svg>/lewis.brand.207</li>
      <li><svg viewBox="0 0 16 16" fill="none" stroke="#fff" stroke-width="1.4"><rect x="1.5" y="3.5" width="13" height="9"/><path d="M1.5 3.5 8 9l6.5-5.5"/></svg>lbrand@fauna812.com.au</li>
    </ul>
    <div class="services-band">
      <span>Equine Performance &nbsp;•&nbsp; Rowland4Ponies and Acupuncture</span>
      <span>Horsemanship Lessons and Clinics &nbsp;•&nbsp; Horse Training</span>
    </div>
  </section>
</body>
</html>
```